Webdesign für Entwickler von onlinebasierten Terminformularen
Super Designs. Schnell und motiviert. Danke für die hervorragende Umsetzung und die Ideen!
Zielgruppe
Deutsch:
Wir sind ein Startup, das über die Seite Kalendrio.de zukünftig folgenden Service anbietet: Unternehmer können sehr flexibel (selbst) gestaltete Terminformulare erstellen und auf Ihrer Website einbinden. Kunden können dann diese Termine buchen und bekommen dann Erinnerungs-Mails und SMS.
Zielgruppe: Dienstleister wie Fotografen, Friseure, Versicherungsvertreter, Masseure, Restaurants, Arztpraxen. Also alle, die darauf angewiesen sind, dass vereinbarte Termine eingehalten werden und die die Terminvereinbarung vereinfachen wollen. Also weniger per Telefon, mehr über die eigene Website.
Englisch:
We are a start up, that is going to offer this services on the Website Kalendrio.de :
Companies can create highly flexible (self-designed) appointment forms and integrate them on their website. Customer can book appointments and will get an reminding email and SMS.
Target group: Service providers such as photographers, hairdressers, insurance agents, masseurs, restaurants, medical offices. So all those who depend on meeting agreed appointments and who want to simplify the appointment. Less by telephone, more over their own website.
Aufgabenstellung
Übersichtlichkeit, genug Weißraum, deutliche, große Überschriften, Seriös aber gerne frische Farben bei einzelnen Elementen (z.B. bei Icons oder bei Handlungsaufforderungs-Buttons), Trennlinien, Inhalte auf den Punkt.
Logo-Entwurf anbei (wird gerade hier über entwurfhafen.de ebenfalls erstellt/optimiert, siehe #817306) sagt das wesentliche aus.
Kalendrio soll also ein sehr nützliches Tool sein, das jeder schnell versteht. Daher muss auch die Website sehr übersichtlich und klar aufgebaut werden. Die wesentlichen Aussagen/Menüpunkte finden sich auf der Startseite (bzw. im Hauptmenü, siehe grober Entwurf anbei).
- frische Farben (z.B. grün, orange, gelb)
- seröse Farben/Grauwerte (z.B. blau, grau, schwarz)
- Hauptmenü/Metanavigation/Footer-Bereich
Das Design und das Teaser-Bild (Frau mit Hammer) auf dem Entwurf anbei (seite1_mit_teaser_entwurf2.jpg) sind nur als grobe Ideen (Richtung) zu verstehen. Die Startseite muss also keine Teaser-Bilder enthalten.
Der Entwurf anbei soll lediglich die ungefähre Richtung mit den angedachten Menüpunkten verdeutlichen.
Übersichtlich und modern finden wir z.B. https://talkroomly.example/de (viel Weißraum, farbige Icons, Infos übersichtlich dargeboten, lächelnde Gesichter) und übrigens auch https://www.entwurfhafen.example.
Bitte entwerfen Sie (erstmal) drei Seiten:
- Startseite
- Funktionen/Preis (Beispiel auf https://talkroomly.example/de/tools Und/oder in Tabellenform wie auf https://talkroomly.example/de/pricing/ siehe Content-Plan anbei)
- Über Kalendrio (Über uns, siehe Content-Plan anbei)
Der Content-Plan soll das Projekt verdeutlichen.
Anmerkung von unserem Programmierer: Praktisch wäre eine Basis auf Bootstrap. Dies ist aber keine Pflicht! Das Design/die Idee geht vor :-)
1zu1-Folgeaufträge (für dieses und andere Projekte im Bereich Webdesign, Flyer, CorporateDesign, Grafiken) sind sehr wahrsc..

```html
<!DOCTYPE html>
<html lang="de">
<head>
<meta charset="utf-8">
<title>Kalendrio – das kostenlose Online-Terminvergabe-Tool</title>
<link rel="stylesheet" href="https://fonts.googleapis.com/css2?family=Jost:ital,wght@0,300;0,400;0,500;0,600;1,300&display=swap">
<style>
:root{
  --green:#8bc043;
  --green-soft:#e8f1e4;
  --ink:#5f676b;
  --ink-dark:#3f474b;
  --muted:#8d9396;
  --bar:#6b7378;
  --footer-top:#6d767b;
  --footer-bottom:#555d62;
  --tile:#f5f6f6;
  --line:#eceeee;
  --white:#ffffff;
}
*{box-sizing:border-box;margin:0;padding:0}
html,body{width:1200px;height:2441px;overflow:hidden}
body{font-family:"Jost",sans-serif;color:var(--ink);background:var(--white);position:relative}
a{color:inherit;text-decoration:none}
.abs{position:absolute}

.meta-bar{position:absolute;top:0;left:0;width:1200px;height:31px;background:var(--bar);color:var(--white);font-size:9px;font-weight:600}
.meta-bar ul{list-style:none;display:flex;position:absolute;right:216px;top:10px;gap:0}
.meta-bar li{padding:0 8px;border-left:1px solid rgba(255,255,255,.4);line-height:11px}
.meta-bar li:first-child{border-left:0}

.main-nav{position:absolute;top:31px;left:0;width:1200px;height:53px;background:var(--white)}
.brand{position:absolute;display:flex;align-items:center;gap:6px;font-weight:500;color:var(--green)}
.brand .mark{width:16px;height:16px;border:2px solid var(--ink);border-radius:3px}
.main-nav .brand{left:237px;top:14px;font-size:23px}
.main-nav .menu{position:absolute;left:377px;top:22px;display:flex;gap:37px;font-size:10px;font-weight:500;color:var(--ink)}
.main-nav .login{position:absolute;left:852px;top:22px;font-size:10px;font-weight:500}
.main-nav .cta{position:absolute;left:890px;top:12px;width:93px;height:29px;border:1.5px solid var(--green);border-radius:15px;font-size:10px;font-weight:500;display:flex;align-items:center;justify-content:center}

.hero{position:absolute;top:84px;left:0;width:1200px;height:400px;background:#f4f4f4;overflow:hidden}
.hero-photo{position:absolute;left:332px;top:0;width:868px;height:400px;background:linear-gradient(90deg,#f4f4f4 0%,#e9e7e5 30%,#d9d3cf 55%,#cfc8c3 75%,#eeeeee 100%)}
.hero-label{position:absolute;left:269px;top:52px;width:343px;height:34px;background:var(--white);font-size:10.5px;font-weight:600;color:var(--ink-dark);display:flex;align-items:center;justify-content:center}
.hero-quote{position:absolute;left:262px;top:102px;width:400px;font-size:20.5px;font-weight:300;line-height:27.5px;color:var(--ink-dark)}
.hero-quote strong{color:var(--green);font-weight:500}
.hero-quote .q{color:var(--muted);font-size:22px;position:absolute}
.hero-author{position:absolute;left:262px;top:231px;font-size:8px;line-height:11px;color:var(--muted)}
.btn{display:flex;align-items:center;justify-content:center;color:var(--white);font-weight:600;background:var(--green)}
.hero-btn{position:absolute;left:257px;top:276px;width:200px;height:43px;font-size:11.5px}
.slider-dots{position:absolute;left:1172px;top:175px;display:flex;flex-direction:column;gap:12px}
.slider-dots span{width:8px;height:8px;border-radius:50%;background:#dcdcdc}
.slider-dots span:first-child{background:var(--green)}

.about-logo{left:237px;top:596px;font-size:33px}
.about-logo .mark{width:26px;height:26px;border-width:3px}
.about-title{left:482px;top:557px;font-size:25px;font-weight:500}
.about-text{left:482px;top:608px;width:500px;font-size:16.5px;font-weight:300;line-height:23.7px}
.about-text b{font-weight:600}
.about-text em{color:var(--muted)}

.divider{position:absolute;left:213px;width:775px;height:1px;background:var(--line)}

.section-head{position:absolute;left:0;width:1200px;text-align:center}
.section-head h2{font-size:25px;font-weight:500;line-height:30px}
.section-head h3{font-size:14.5px;font-weight:500;margin-top:2px}
.section-head .rule{width:50px;height:2px;background:var(--green);margin:12px auto 0}
.section-head p{font-size:11.5px;font-weight:300;line-height:23.7px;margin-top:24px}

.feature-art{left:216px;top:1155px;width:320px;height:282px;border-radius:8px;background:linear-gradient(135deg,#ffffff 0%,#f1f2f2 60%,#e6eae3 100%)}
.feature-list{position:absolute;left:627px;top:1088px;width:353px;list-style:none}
.feature-list li{height:47px;margin-bottom:13px;background:var(--tile);display:flex;align-items:center;padding-left:16px;gap:12px;font-size:13px;font-weight:500}
.feature-list li.active{background:var(--green-soft)}
.feature-list svg{width:22px;height:22px;flex:none}
.feature-btn{position:absolute;left:627px;top:1467px;width:353px;height:50px;font-size:11.5px}

.service-card{position:absolute;top:1917px;width:375px;height:244px;background:var(--tile);overflow:hidden}
.service-card h4{position:absolute;left:38px;top:38px;font-size:18.5px;font-weight:500;line-height:24px}
.service-card p{position:absolute;left:38px;top:119px;font-size:9.5px;font-weight:300;line-height:15px;color:var(--ink-dark)}
.service-card .card-btn{position:absolute;left:38px;top:164px;height:43px;background:var(--bar);color:var(--white);font-size:11.5px;font-weight:600;display:flex;align-items:center;padding:0 20px 0 16px;gap:10px}
.service-card .card-btn i{color:var(--green);font-style:normal;font-weight:400}
.service-card .art{position:absolute;right:0;top:0;width:175px;height:244px;background:linear-gradient(160deg,#f5f6f6 0%,#ffffff 45%,#e9ebec 100%)}

.footer-top{position:absolute;top:2230px;left:0;width:1200px;height:68px;background:var(--footer-top)}
.footer-top .brand{left:214px;top:20px;font-size:22px;color:var(--white)}
.footer-top .brand .mark{border-color:var(--white)}
.footer-bottom{position:absolute;top:2298px;left:0;width:1200px;height:143px;background:var(--footer-bottom);color:var(--white)}
.footer-bottom .copy{position:absolute;left:214px;top:19px;font-size:9px;font-weight:600}
.lang-pill{position:absolute;left:214px;top:51px;width:144px;height:31px;border:1px solid rgba(255,255,255,.6);border-radius:16px;font-size:9.5px;font-weight:600;display:flex;align-items:center;justify-content:center;gap:14px}
.footer-col{position:absolute;top:19px;font-size:9px;line-height:17.5px}
.footer-col h5{font-size:9px;font-weight:600;margin-bottom:5px}
.footer-col ul{list-style:none;color:#e1e4e5}
.rating p{font-size:7.5px;line-height:12px;color:#e1e4e5;width:180px}
.rating-btn{position:absolute;left:801px;top:84px;width:181px;height:37px;font-size:10px}
</style>
</head>
<body>

<header class="meta-bar">
  <ul>
    <li>Kontakt</li>
    <li>DE ⌵</li>
    <li>Zu Votewerk wechseln</li>
  </ul>
</header>

<nav class="main-nav">
  <a class="brand"><span class="mark"></span>Kalendrio</a>
  <div class="menu"><a>Funktionen / Preis</a><a>Help-Center</a><a>Über Uns</a><a>Blog</a></div>
  <a class="login">Login</a>
  <a class="cta">Konto erstellen</a>
</nav>

<section class="hero">
  <div class="hero-photo" role="img" aria-label="Foto: lächelnde Friseurin mit verschränkten Armen und Schere im Salon"></div>
  <div class="hero-label">Kalendrio – das kostenlose Online-Terminvergabe-Tool</div>
  <blockquote class="hero-quote">
    <span class="q" style="left:-18px;top:-8px">"</span>
    &nbsp;Im Salon ist die Schere mein Werkzeug.<br>
    &nbsp;An <strong>Kalendrio</strong> gefällt mir besonders die<br>
    &nbsp;automatische Terminerinnerung per SMS<br>
    &nbsp;und Email für meine Kunden.
    <span class="q" style="left:270px;top:92px">"</span>
  </blockquote>
  <div class="hero-author">Lena, Friseurmeisterin<br>aus Hamburg</div>
  <a class="btn hero-btn">Jetzt kostenlos starten</a>
  <div class="slider-dots"><span></span><span></span><span></span></div>
</section>

<div class="brand about-logo abs"><span class="mark"></span>Kalendrio</div>
<h2 class="about-title abs">Was ist Kalendrio?</h2>
<p class="about-text abs">Kalendrio wurde aus der Not geboren.<br>"Wir benötigen selbst ein flexibles Tool, dass uns die <b>lästige</b> und <b>zeitraubende</b> Arbeit bei der Terminvereinbarung abnimmt."<br><em>Jonas Berger, Inhaber &amp; Gründer</em></p>

<div class="divider" style="top:799px"></div>

<div class="section-head" style="top:874px">
  <h2>Funktionen</h2>
  <h3>Kalendrio – das kostenlose Online-Terminvergabe-Tool</h3>
  <div class="rule"></div>
  <p>Kalendrio ist ein einfaches &amp; bequemes Tool für eine schnelle, unkomplizierte Terminvergabe sowohl für<br>Ihre Kunden als auch für Sie, mit praktischer Email und SMS-Reminder Funktion.</p>
</div>

<div class="feature-art abs" role="img" aria-label="Illustration: zwei Terminformular-Karten mit Kalender- und Glockensymbol"></div>

<ul class="feature-list">
  <li><svg viewBox="0 0 22 22" fill="none" stroke="#5f676b" stroke-width="1.4"><rect x="2" y="5" width="16" height="13"/><path d="M4 15l4-4 3 3 2-2 4 3" stroke="#8bc043"/></svg>Umfragen mit Teaser-Foto / Streamtube-Video</li>
  <li><svg viewBox="0 0 22 22"><rect x="2" y="3" width="18" height="5" fill="none" stroke="#8bc043" stroke-width="1.4"/><rect x="2" y="10" width="18" height="4" fill="none" stroke="#8bc043" stroke-width="1.4"/><rect x="2" y="16" width="18" height="4" fill="#8bc043"/></svg>Formular-Generator</li>
  <li class="active"><svg viewBox="0 0 22 22" fill="none" stroke="#3f474b" stroke-width="1.5"><rect x="2" y="4" width="18" height="16" rx="1"/><path d="M6 2v4M16 2v4M2 8h18M7 14l3 3 6-6"/></svg>Termin-Assistent (Wizzard)</li>
  <li><svg viewBox="0 0 22 22" fill="none" stroke="#8bc043" stroke-width="1.4"><circle cx="5" cy="8" r="3"/><circle cx="5" cy="16" r="3"/><path d="M8 9l12 6M8 15l12-6"/></svg>Branchenspezifische Vorlagen</li>
  <li><svg viewBox="0 0 22 22" fill="none" stroke="#8bc043" stroke-width="1.4"><rect x="3" y="2" width="14" height="18"/><circle cx="10" cy="10" r="3.5"/><path d="M12.5 12.5l4 4"/></svg>Termin-Verwaltung und Terminübersicht</li>
  <li><svg viewBox="0 0 22 22" fill="none" stroke="#8bc043" stroke-width="1.2"><rect x="1" y="3" width="9" height="9"/><rect x="12" y="3" width="9" height="9"/><path d="M11 12v8M8 17l3 3 3-3"/></svg>Teilnehmerliste als CSV / PDF-Export</li>
</ul>
<a class="btn feature-btn">Jetzt kostenlos Konto erstellen</a>

<div class="divider" style="top:1628px"></div>

<div class="section-head" style="top:1703px">
  <h2>Kalendrio – Service</h2>
  <h3>Haben Sie Fragen oder möchten immer auf dem Laufenden bleiben?</h3>
  <div class="rule"></div>
  <p>Dann nutzen Sie gerne unsere Service-Angebote. In unserem Help-Center finden Sie sicher eine Lösung<br>für Ihre Probleme und im Blog finden Sie die aktuellsten Neuigkeiten rund um Kalendrio.</p>
</div>

<article class="service-card" style="left:216px">
  <div class="art" role="img" aria-label="Illustration: gekippte Karten mit Fragezeichen-Symbolen"></div>
  <h4>Kalendrio<br>Help-Center</h4>
  <p>Sie haben Fragen? Dann nutzen Sie<br>gerne unser Help-Center.</p>
  <a class="card-btn"><i>›</i>Weiter zum Help-Center</a>
</article>
<article class="service-card" style="left:609px">
  <div class="art" role="img" aria-label="Illustration: gestapelte Blog-Artikel-Karten"></div>
  <h4>Kalendrio<br>News Blog</h4>
  <p>Bleiben Sie immer auf dem Laufenden<br>&amp; erfahren Sie alle Neuigkeiten.</p>
  <a class="card-btn"><i>›</i>Weiter zum Kalendrio-Blog</a>
</article>

<footer>
  <div class="footer-top"><a class="brand"><span class="mark"></span>Kalendrio</a></div>
  <div class="footer-bottom">
    <div class="copy">© 2018 Alle Rechte vorbehalten</div>
    <div class="lang-pill"><span>Sprachauswahl</span><span>DE ⌵</span></div>
    <div class="footer-col" style="left:492px"><h5>Sonstiges</h5><ul><li>Home</li><li>Kontakt</li><li>Newsletter</li><li>Webinare</li></ul></div>
    <div class="footer-col" style="left:574px"><h5>Benutzer</h5><ul><li>Login</li><li>Konto erstellen</li></ul></div>
    <div class="footer-col" style="left:671px"><h5>Rechtliches</h5><ul><li>Impressum</li><li>AGB</li><li>Datenschutz</li><li>Sitemap</li></ul></div>
    <div class="footer-col rating" style="left:799px"><h5>Bewertungen durch Votewerk.de</h5><p>Verknüpfen Sie jetzt Kalendrio<br>mit Votewerk.de und profitieren Sie von<br>vertrauensvollen Usern und Transparenz.</p></div>
    <a class="btn rating-btn">zu Votewerk.de wechseln</a>
  </div>
</footer>

</body>
</html>
```